PowerPoint Template Needed for Investment Firm

Meridale Capital Management is an emerging wealth management firm based in New Jersey. It offers superior investment returns to high net worth individuals and institutions by finding undervalued assets.

We recently selected a company logo which was inspired by the Meridale constellation. Beta Tucanae is a group of six stars, containing star cluster 47 Tucanae, rated the second brightest object in the sky.

Now we need a PowerPoint template with the designs for the following:

1. Title/cover page slide
2. Content slide with title
3. Section slide - to introduce a new section
4. Final slide - with contact information

The slides will be used at investor presentations, that is, to provide information about the company to potential investors. Since we are an investment firm, the design should project a sense of stability, growth and professionalism. The owner is interested in something simple yet striking, which of course is consistent with the logo. I'm thinking more conservative colors and Sans Serif fonts.

I plan on changing the status to non-refundable once I see some designs that I really like.

Target Market(s)

Wealthy individuals, probably middle aged or older, in the US

Industry/Entity Type

Conservative

Requirements
Must have
• Sans serif fonts
Clean, very professional look
Conservative colors that complement existing logo
Should not have
• Anything too busy or complicated

```html
<!DOCTYPE html>
<html lang="en">
<head>
<meta charset="utf-8">
<title>Meridale Capital Management – Contact</title>
<link rel="stylesheet" href="https://fonts.googleapis.com/css2?family=Arimo:wght@400&display=swap">
<style>
  :root {
    --frame-blue: #1240a8;
    --page-white: #ffffff;
    --panel-border: #c9c9c9;
    --ink: #000000;
    --photo-light: #f4f4f2;
    --photo-mid: #d9d6d0;
  }
  * { margin: 0; padding: 0; box-sizing: border-box; }
  html, body { width: 1200px; height: 901px; overflow: hidden; background: var(--page-white); }
  .slide {
    position: relative;
    width: 1200px;
    height: 901px;
    background: var(--frame-blue);
    font-family: "Arimo", Arial, sans-serif;
  }
  .slide-surface {
    position: absolute;
    left: 19px; top: 23px; right: 19px; bottom: 23px;
    background: var(--page-white);
    border-radius: 24px;
    overflow: hidden;
  }
  .contact-photo {
    position: absolute;
    left: 762px; top: 0; width: 400px; height: 278px;
    background: linear-gradient(100deg, var(--page-white) 0%, var(--photo-light) 45%, var(--photo-mid) 100%);
  }
  .contact-card {
    position: absolute;
    left: 152px; top: 229px;
    width: 892px; height: 495px;
  }
  .contact-card svg { position: absolute; inset: 0; }
  .contact-details {
    position: absolute;
    left: 44px; top: 90px;
    font-size: 46px;
    line-height: 61px;
    color: var(--ink);
    letter-spacing: -0.3px;
  }
  .page-number {
    position: absolute;
    left: 1148px; top: 836px;
    font-size: 21px;
    color: var(--ink);
  }
</style>
</head>
<body>
  <div class="slide">
    <div class="slide-surface">
      <div class="contact-photo" role="img" aria-label="Photo of a hand writing the words Contact us with a marker"></div>
    </div>

    <div class="contact-card">
      <svg width="892" height="495" viewBox="0 0 892 495">
        <polygon points="0,0 100,0 0,98" fill="var(--frame-blue)"/>
        <polygon points="892,0 792,0 892,92" fill="var(--frame-blue)"/>
        <polygon points="0,495 100,495 0,410" fill="var(--frame-blue)"/>
        <polygon points="892,495 792,495 892,410" fill="var(--frame-blue)"/>
        <rect x="16" y="15" width="845" height="464" fill="var(--page-white)" stroke="var(--panel-border)" stroke-width="2"/>
      </svg>
      <address class="contact-details" style="font-style:normal">
        48 Harbor Ave.<br>
        Newark,<br>
        NJ 07102,<br>
        www.meridalecapmgmt.com,<br>
        jcarter@meridalecapmgmt.com
      </address>
    </div>

    <div class="page-number">4</div>
  </div>
</body>
</html>
```